Business Cards for Tech Company - uBrightowl

We would like new modern business cards designed for our company. Attached are some examples of other business cards we like. <br/><br/>Info we need is: <br/>First Name, Last Name<br/>Address<br/>Store Phone<br/>Cell Phone<br/>Email Address<br/>Text Logo <br/>And Other Logo<br/>

Industry/Entity Type

Technology Equipment

Contact Information for Business Card

Please use these details as example:

Dale Morrow
Technology Specialist
Direct 555.617.2094
Phone 555-730-8186

dale.morrow@ubrightowl.example

2971 Willet Lane
Larkfield, NV 00427

Font styles to use
Sans Serif
Other font styles liked:
• Anything easy to read and modern

Colors

Designer to choose colors to be used in the design.

Requirements
Must have
• Both Logos
• Signature as name
• Use the text logo and use the shark logo but do not use the full shark logo. Have it where it is zoomed in and is expanding out of the card.
Nice to have
• Keep it clean and modern
• We like blue, white, and black/grays.
Should not have
• Random icons for phone and address.

```html
<!DOCTYPE html>
<html lang="en">
<head>
<meta charset="utf-8">
<title>uBrightowl Business Cards</title>
<link rel="stylesheet" href="https://fonts.googleapis.com/css2?family=Roboto:wght@400;500;900&family=Nothing+You+Could+Do&display=swap">
<style>
  :root {
    --bg: #4a4a4a;
    --card-white: #ffffff;
    --brand-blue: #4272b8;
    --brand-cyan: #33b8e6;
    --back-start: #4474b9;
    --back-end: #34bde8;
    --ink-gray: #5f6064;
    --mark-gray: #6c6d71;
    --logo-gray: #656565;
  }
  html, body {
    margin: 0;
    width: 1200px;
    height: 1200px;
    overflow: hidden;
    background: var(--bg);
  }
  .canvas {
    position: relative;
    width: 1200px;
    height: 1200px;
  }
  .card {
    position: absolute;
    left: 120px;
    width: 960px;
    height: 549px;
    border-radius: 28px;
    overflow: hidden;
    box-shadow: 0 14px 30px rgba(0,0,0,0.35);
  }
  .card-back {
    top: 34px;
    background: linear-gradient(115deg, var(--back-start) 0%, #3d9bd3 50%, var(--back-end) 100%);
  }
  .card-front {
    top: 617px;
    background: var(--card-white);
  }
  .card-art {
    position: absolute;
    inset: 0;
    width: 100%;
    height: 100%;
  }
  .back-wordmark {
    position: absolute;
    left: 0;
    right: 0;
    top: 220px;
    text-align: center;
    font-family: "Roboto", sans-serif;
    font-weight: 900;
    font-size: 96px;
    letter-spacing: -2px;
    color: #ffffff;
  }
  .front-wordmark {
    position: absolute;
    left: 60px;
    top: 44px;
    font-family: "Roboto", sans-serif;
    font-weight: 900;
    font-size: 70px;
    letter-spacing: -1.5px;
    color: var(--logo-gray);
  }
  .contact {
    position: absolute;
    left: 70px;
    top: 160px;
    font-family: "Roboto", sans-serif;
    color: var(--ink-gray);
  }
  .signature {
    font-family: "Nothing You Could Do", cursive;
    font-size: 58px;
    line-height: 1;
    color: var(--brand-blue);
    margin: 0 0 0 20px;
  }
  .job-title {
    font-weight: 500;
    font-size: 25px;
    color: var(--brand-cyan);
    margin: 4px 0 18px;
  }
  .address {
    font-size: 25px;
    line-height: 1.3;
    margin: 0 0 16px 6px;
  }
  .contact-line {
    display: flex;
    align-items: center;
    gap: 10px;
    font-size: 25px;
    line-height: 1.35;
  }
  .contact-icon {
    width: 20px;
    height: 20px;
    flex: none;
  }
</style>
</head>
<body>
<div class="canvas">

  <section class="card card-back">
    <svg class="card-art" viewBox="0 0 960 549">
      <defs>
        <linearGradient id="backMarkFade" x1="0" y1="0" x2="1" y2="1">
          <stop offset="0" stop-color="#3aa6dc" stop-opacity="0.6"/>
          <stop offset="1" stop-color="#35c2ea" stop-opacity="0.9"/>
        </linearGradient>
      </defs>
      <path role="img" aria-label="Faint enlarged brand mark decoration rising from the card edge"
            d="M960 60 C820 90 700 200 660 330 C640 420 650 500 680 549 L960 549 Z"
            fill="url(#backMarkFade)"/>
    </svg>
    <div class="back-wordmark">uBrightowl</div>
  </section>

  <section class="card card-front">
    <svg class="card-art" viewBox="0 0 960 549">
      <defs>
        <linearGradient id="frontMarkFill" x1="0" y1="0" x2="1" y2="0">
          <stop offset="0" stop-color="#ffffff"/>
          <stop offset="0.45" stop-color="#e4e5e7"/>
          <stop offset="1" stop-color="#6c6d71"/>
        </linearGradient>
      </defs>
      <path class="swoosh-band" fill="var(--brand-blue)"
            d="M700 0 L900 0 C760 60 640 180 620 330 C610 420 630 500 660 549 L560 549
               C520 440 510 330 540 230 C570 130 630 50 700 0 Z"/>
      <path role="img" aria-label="Zoomed-in brand mark illustration expanding out of the card edge"
            d="M900 0 L960 0 L960 549 L660 549 C630 500 610 420 620 330 C640 180 760 60 900 0 Z"
            fill="url(#frontMarkFill)"/>
    </svg>

    <div class="front-wordmark">uBrightowl</div>

    <div class="contact">
      <p class="signature">Dale Morrow</p>
      <p class="job-title">Technology Specialist</p>
      <p class="address">2971 Willet Lane<br>Larkfield, NV 00427</p>
      <div class="contact-line">
        <svg class="contact-icon" viewBox="0 0 20 20"><circle cx="10" cy="10" r="10" fill="var(--brand-blue)"/><path d="M7 5 L9 5 L9.6 8 L8.4 9 C9 10.6 9.8 11.4 11 12 L12 10.8 L15 11.4 L15 13.4 C11 14 6 9 7 5 Z" fill="#fff"/></svg>
        <span>555.617.2094 (Direct)</span>
      </div>
      <div class="contact-line">
        <svg class="contact-icon" viewBox="0 0 20 20"><circle cx="10" cy="10" r="10" fill="var(--brand-blue)"/><path d="M7 5 L9 5 L9.6 8 L8.4 9 C9 10.6 9.8 11.4 11 12 L12 10.8 L15 11.4 L15 13.4 C11 14 6 9 7 5 Z" fill="#fff"/></svg>
        <span>555-730-8186</span>
      </div>
      <div class="contact-line">
        <svg class="contact-icon" viewBox="0 0 20 20"><circle cx="10" cy="10" r="10" fill="var(--brand-blue)"/><circle cx="10" cy="10" r="5.5" fill="none" stroke="#fff" stroke-width="1.3"/><ellipse cx="10" cy="10" rx="2.4" ry="5.5" fill="none" stroke="#fff" stroke-width="1.1"/><line x1="4.5" y1="10" x2="15.5" y2="10" stroke="#fff" stroke-width="1.1"/></svg>
        <span>dale.morrow@ubrightowl.example</span>
      </div>
    </div>
  </section>

</div>
</body>
</html>
```